Verdant Holdings SA Business Cards

Dear all,
Thank you for reading my brief and project. My company is doing doing advisory in real estate and to comapnies + real estates services as asset management, brokerage, development etc.
I would like to get a business card for my company which is clear, professionnal and serious.
Please have a look to the attachement to see the logos of the company

Industry/Entity Type

Real Estate

Contact Information for Business Card

I would like to have in the business card the following
Principal side:
- Logo of the company (or Monogram)
- First and Last Name (Marcel Tobler)
- Mobile number
- email address

Second side:
- Address (Chemin des Vergers 17, 1292 Chambésy - Switzerland)
- website (www.verdantholdings.ch)

Requirements
Must have
• Refer to the typeface and logo colors

```html
<!DOCTYPE html>
<html lang="en">
<head>
<meta charset="utf-8">
<title>Verdant Holdings SA – Business Cards</title>
<link href="https://fonts.googleapis.com/css2?family=Work+Sans:wght@400;500;600&display=swap" rel="stylesheet">
<style>
  :root {
    --bg: #1f1f20;
    --slate: #414e61;
    --slate-light: #4c596b;
    --blue: #1674c6;
    --ink: #3b4452;
    --white: #ffffff;
  }
  * { box-sizing: border-box; margin: 0; padding: 0; }
  html, body { width: 1200px; height: 900px; overflow: hidden; }
  body {
    background: var(--bg);
    font-family: "Work Sans", Arial, sans-serif;
    position: relative;
  }
  .card {
    position: absolute;
    left: 270px;
    width: 660px;
    height: 378px;
    overflow: hidden;
  }
  .card--front {
    top: 52px;
    background: linear-gradient(135deg, var(--slate) 0%, var(--slate-light) 100%);
    display: flex;
    align-items: center;
    justify-content: center;
  }
  .brand {
    display: flex;
    align-items: center;
    gap: 18px;
  }
  .brand__mark {
    width: 22px;
    height: 22px;
    background: var(--blue);
  }
  .brand__name {
    color: var(--white);
    font-weight: 500;
    font-size: 30px;
    letter-spacing: 2px;
    text-transform: uppercase;
  }
  .card--back {
    top: 470px;
    background: var(--white);
  }
  .identity {
    position: absolute;
    top: 128px;
    right: 340px;
    text-align: right;
  }
  .identity__name {
    color: var(--blue);
    font-size: 34px;
    font-weight: 500;
    line-height: 1.1;
  }
  .identity__name strong { font-weight: 600; }
  .identity__role {
    color: var(--ink);
    font-size: 19px;
    margin-top: 4px;
    letter-spacing: 0.5px;
  }
  .divider {
    position: absolute;
    left: 340px;
    top: 128px;
    width: 2px;
    height: 74px;
    background: var(--blue);
  }
  .contact {
    position: absolute;
    left: 362px;
    top: 128px;
    list-style: none;
    color: var(--ink);
    font-size: 18px;
    line-height: 25px;
    letter-spacing: 0.4px;
  }
  .contact__item { display: flex; align-items: center; gap: 8px; }
  .contact__icon { width: 13px; height: 13px; flex: none; }
  .address-band {
    position: absolute;
    left: 0;
    right: 0;
    bottom: 14px;
    height: 40px;
    background: var(--slate);
    color: var(--white);
    font-size: 19px;
    letter-spacing: 0.6px;
    display: flex;
    align-items: center;
    padding-left: 44px;
  }
</style>
</head>
<body>
  <section class="card card--front">
    <div class="brand">
      <span class="brand__mark"></span>
      <span class="brand__name">Verdant Holdings</span>
    </div>
  </section>

  <section class="card card--back">
    <div class="identity">
      <p class="identity__name"><strong>Marcel</strong> Tobler</p>
      <p class="identity__role">Principal</p>
    </div>
    <span class="divider"></span>
    <ul class="contact">
      <li class="contact__item">
        <svg class="contact__icon" viewBox="0 0 16 16"><path d="M4 1.5 6.3 4 5 5.8c.9 2 2.6 3.7 4.6 4.6L11.4 9l2.6 2.3-1.3 2.3C7 13.8 2.2 9 2.1 3.3z" fill="none" stroke="#1674c6" stroke-width="1.5" stroke-linejoin="round"/></svg>
        +41 22 555 01 84
      </li>
      <li class="contact__item">
        <svg class="contact__icon" viewBox="0 0 16 16"><rect x="1.5" y="3.5" width="13" height="9" fill="none" stroke="#1674c6" stroke-width="1.5"/><path d="M1.5 3.5 8 9l6.5-5.5" fill="none" stroke="#1674c6" stroke-width="1.5"/></svg>
        info@verdantholdings.ch
      </li>
      <li class="contact__item">
        <svg class="contact__icon" viewBox="0 0 16 16"><g fill="none" stroke="#1674c6" stroke-width="1.3"><circle cx="8" cy="8" r="6.3"/><ellipse cx="8" cy="8" rx="2.8" ry="6.3"/><path d="M1.7 8h12.6M2.6 5h10.8M2.6 11h10.8"/></g></svg>
        www.verdantholdings.ch
      </li>
    </ul>
    <div class="address-band">Chemin des Vergers 17, 1292 Chambésy - Switzerland</div>
  </section>
</body>
</html>
```